Upmarket Dessert Lounge needs a Business Card Design

We are an upmarket dessert lounge needing a business card to match our image.

We want something that is simple yet beautiful, feminine, classy, sophisticated and elegant. We want it to stand out and don't mind if it is bold.

The design should include our logo and colours of red or maroon with gold highlights. We don't mind if black is used.

Marlow & Quince

Target Market(s)

For those who like to indulge or treat themselves and give in to their temptations on good quality desserts.

Industry/Entity Type

Business

Requirements
Must have
• Must include our logo and our name

Marlow & Quince

M & Q

```html
<!DOCTYPE html>
<html lang="en">
<head>
<meta charset="utf-8">
<title>Marlow &amp; Quince – Business Card</title>
<link href="https://fonts.googleapis.com/css2?family=Noto+Serif:wght@400&display=swap" rel="stylesheet">
<style>
  :root {
    --backdrop: #dfe3e6;
    --maroon: #8a2424;
    --maroon-deep: #7a1d1e;
    --damask-light: #932b2a;
    --gold: #f3dcaa;
    --shadow: rgba(40, 30, 30, 0.25);
  }
  * { box-sizing: border-box; margin: 0; padding: 0; }
  html, body {
    width: 1200px;
    height: 960px;
    overflow: hidden;
    background: var(--backdrop);
    font-family: "Noto Serif", Georgia, serif;
  }
  .sheet {
    width: 1200px;
    height: 960px;
    display: flex;
    flex-direction: column;
    align-items: center;
    justify-content: center;
    gap: 40px;
  }
  .card {
    position: relative;
    width: 700px;
    height: 400px;
    background: var(--maroon);
    color: var(--gold);
    box-shadow: 0 8px 24px var(--shadow);
    overflow: hidden;
  }

  /* Front: contact side */
  .card-front .holder {
    position: absolute;
    left: 52px;
    top: 118px;
  }
  .holder-name { font-size: 31px; line-height: 1.2; }
  .holder-role { font-size: 19px; margin-top: 10px; }

  .brand-mark {
    position: absolute;
    right: 52px;
    top: 56px;
    width: 190px;
    text-align: center;
    font-size: 50px;
    line-height: 1;
  }

  .contact-list {
    position: absolute;
    left: 56px;
    bottom: 56px;
    list-style: none;
    font-size: 19px;
  }
  .contact-list li {
    display: flex;
    align-items: center;
    gap: 14px;
    height: 30px;
  }
  .contact-list svg { width: 18px; height: 18px; flex: none; }

  .address {
    position: absolute;
    right: 40px;
    bottom: 88px;
    font-size: 15.5px;
    line-height: 1.45;
    font-style: normal;
  }

  /* Back: brand side */
  .card-back .damask {
    position: absolute;
    inset: 0;
    background: radial-gradient(circle at 50% 50%, var(--damask-light), var(--maroon-deep));
  }
  .card-back .brand-name {
    position: absolute;
    inset: 0;
    display: flex;
    align-items: center;
    justify-content: center;
    font-size: 44px;
    letter-spacing: 2px;
    text-transform: uppercase;
  }
</style>
</head>
<body>
<main class="sheet">

  <section class="card card-front" aria-label="Business card front">
    <div class="holder">
      <p class="holder-name">Name Surname</p>
      <p class="holder-role">Manager</p>
    </div>

    <p class="brand-mark">M &amp; Q</p>

    <ul class="contact-list">
      <li>
        <svg viewBox="0 0 18 18" fill="none" stroke="currentColor" stroke-width="1.4" aria-hidden="true">
          <rect x="3" y="2" width="12" height="14" rx="1"/>
          <rect x="5" y="4" width="3" height="10"/>
          <line x1="10" y1="6" x2="13" y2="6"/>
          <line x1="10" y1="9" x2="13" y2="9"/>
          <line x1="10" y1="12" x2="13" y2="12"/>
        </svg>
        <span>(555) 01 234 56 78</span>
      </li>
      <li>
        <svg viewBox="0 0 18 18" fill="none" stroke="currentColor" stroke-width="1.4" aria-hidden="true">
          <rect x="5" y="2" width="8" height="5"/>
          <rect x="2" y="7" width="14" height="6" rx="1"/>
          <rect x="5" y="11" width="8" height="5" fill="currentColor"/>
        </svg>
        <span>(555) 01 234 56 79</span>
      </li>
      <li>
        <svg viewBox="0 0 18 18" fill="none" stroke="currentColor" stroke-width="1.4" aria-hidden="true">
          <rect x="2" y="4" width="14" height="10"/>
          <polyline points="2,4 9,10 16,4"/>
        </svg>
        <span>info@marlow-quince.com</span>
      </li>
    </ul>

    <address class="address">
      Rue des Tilleuls - Parc Haut<br>
      BP 412 - City, Country<br>
      www.marlow-quince.com
    </address>
  </section>

  <section class="card card-back" aria-label="Business card back">
    <div class="damask" role="img" aria-label="Tone-on-tone maroon damask scroll pattern covering the card"></div>
    <p class="brand-name">Marlow &amp; Quince</p>
  </section>

</main>
</body>
</html>
```